Business card design needed

Family General Practitioner/ Family Physician.
Logo is the logo of the Crestmoor Guild of Family Clinicians Australia
http://kvplm.tarevo.edu.au/PictureGallery/logos/pages/CGFC%20logo_jpg.htm

Reason: Just a bit more time to make changes and the weekend for me to look at things closely and to choose. Thanks, Lumi

Thanks for all the submissions. So many of them are really works of art. Not one of them are not good. The ones that I am eliminating are the ones that I think are not suitable for me personally only, and because if I don't, it makes it very difficult to decide as many of you are also sending me slight variations of a card. I have just decided to choose a second place card too. Can't thank you all enough. Good luck, Lumi. P.S - Working today till 10 pm as the card says :-), so probably won't be able to give a feedback till late Saturday night or Sunday morning here in Sydney, Australia. 

Reason: Just added a second place to the budget and realised that Australia is ahead of the rest of the world in the time zone (only :-) - don't want to offend anyone or start a debate!! ) , so Monday deadline will mean it will be a weekend for the rest of the world. Just wanted to give everyone more time to submit their best, especially since I will be picking a second card too. Can't thank everyone enough for the submissions. P.S - Not keen on photos on the card.

Contact Information for Business Card

Dr. Lumi Harcourt M.B.B.S., F.C.G.F.C
Family General Practitioner
Address, timings, phone and fax number on the back.

Requirements
Must have
• Timings
Mon 7 am - 7 pm
Tues 7 am - 12 pm
Wed 7 am - 10 pm
Thurs 7 am - 12 pm
Fri 7 am - 8 pm
Sat 8 am - 10 pm
Sun - Off

```html
<!DOCTYPE html>
<html lang="en">
<head>
<meta charset="utf-8">
<title>Dr Lumi Harcourt – Business Card</title>
<link href="https://fonts.googleapis.com/css2?family=Tinos:wght@400;700&display=swap" rel="stylesheet">
<style>
  :root {
    --canvas-bg: #eceff3;
    --card-bg: #ffffff;
    --brand-blue: #1b8fd8;
    --brand-blue-light: #6cc0ef;
    --brand-blue-pale: #cfe9f8;
    --ink: #3a3a3a;
    --ink-soft: #555555;
    --mark-ink: #5a6b7a;
    --watermark: #e9edf1;
  }
  * { box-sizing: border-box; margin: 0; padding: 0; }
  html, body {
    width: 1200px; height: 340px; overflow: hidden;
    background: var(--canvas-bg);
    font-family: "Tinos", "Times New Roman", serif;
    color: var(--ink);
  }
  .sheet { position: relative; width: 1200px; height: 340px; }
  .card {
    position: absolute; top: 2px;
    width: 514px; height: 336px;
    background: var(--card-bg);
    overflow: hidden;
  }
  .card--front { left: 75px; }
  .card--back { left: 611px; }
  .card__waves { position: absolute; inset: 0; width: 100%; height: 100%; }

  .watermark {
    position: absolute;
    font-size: 96px; font-weight: 700;
    color: var(--watermark);
    letter-spacing: 2px;
  }
  .card--front .watermark { left: 250px; top: 70px; }
  .card--back .watermark { left: 330px; top: 100px; font-size: 80px; }

  .org-mark {
    position: absolute; left: 38px; top: 110px;
    display: flex; align-items: center; gap: 10px;
    font-size: 40px; font-weight: 700; color: var(--mark-ink);
  }
  .org-mark__square { width: 18px; height: 18px; background: var(--mark-ink); }

  .identity {
    position: absolute; left: 270px; top: 156px; width: 220px;
    text-align: center;
  }
  .identity__name { font-size: 31px; font-weight: 400; color: var(--ink); line-height: 1; }
  .identity__credentials { font-size: 12px; color: var(--ink-soft); margin-top: 3px; letter-spacing: .3px; }
  .identity__role { font-size: 19px; color: var(--ink); margin-top: 1px; }

  .hours { position: absolute; left: 22px; top: 84px; }
  .hours__title { font-size: 16px; margin-bottom: 6px; }
  .hours__table { border-collapse: collapse; font-size: 15px; }
  .hours__table td { padding: 2px 0; height: 22.5px; }
  .hours__day { width: 50px; padding-left: 12px !important; }

  .address {
    position: absolute; left: 302px; top: 236px;
    font-size: 12.5px; line-height: 17.5px; color: var(--ink);
  }
  .address__sep { display: inline-block; width: 1px; height: 11px; background: var(--ink); margin: 0 4px; vertical-align: -1px; }
  .pin-icon { position: absolute; left: 306px; top: 212px; width: 20px; height: 20px; }
</style>
</head>
<body>
<main class="sheet">

  <section class="card card--front" aria-label="Card front">
    <span class="watermark" aria-hidden="true">CGFC</span>
    <svg class="card__waves" viewBox="0 0 352 230" preserveAspectRatio="none" aria-hidden="true">
      <path d="M0,0 H352 V30 C270,8 150,18 0,52 Z" fill="var(--brand-blue-light)"/>
      <path d="M0,0 H352 V14 C270,-2 140,10 0,34 Z" fill="var(--brand-blue)"/>
      <path d="M0,192 C120,178 230,200 352,168 V230 H0 Z" fill="var(--brand-blue-pale)"/>
      <path d="M0,200 C120,188 230,210 352,178 V230 H0 Z" fill="var(--brand-blue)"/>
    </svg>
    <div class="org-mark"><span class="org-mark__square"></span>CGFC</div>
    <div class="identity">
      <h1 class="identity__name">Dr&nbsp;&nbsp;Lumi Harcourt</h1>
      <p class="identity__credentials">M.B.B.S., F.C.G.F.C</p>
      <p class="identity__role">Family General Practitioner</p>
    </div>
  </section>

  <section class="card card--back" aria-label="Card back">
    <span class="watermark" aria-hidden="true">CGFC</span>
    <svg class="card__waves" viewBox="0 0 352 230" preserveAspectRatio="none" aria-hidden="true">
      <path d="M0,0 H352 V46 C260,18 120,14 0,26 Z" fill="var(--brand-blue-light)"/>
      <path d="M0,0 H352 V34 C260,8 120,4 0,16 Z" fill="var(--brand-blue)"/>
      <path d="M0,218 C120,214 240,220 352,208 V230 H0 Z" fill="var(--brand-blue-pale)"/>
      <path d="M0,224 C120,220 240,226 352,216 V230 H0 Z" fill="var(--brand-blue)"/>
    </svg>
    <div class="hours">
      <h2 class="hours__title" style="font-weight:400">Working Hours</h2>
      <table class="hours__table">
        <tr><td class="hours__day">Mon</td><td>7 am - 7 pm</td></tr>
        <tr><td class="hours__day">Tues</td><td>7 am - 12 pm</td></tr>
        <tr><td class="hours__day">Wed</td><td>7 am - 10 pm</td></tr>
        <tr><td class="hours__day">Thurs</td><td>7 am - 12 pm</td></tr>
        <tr><td class="hours__day">Fri</td><td>7 am - 8 pm</td></tr>
        <tr><td class="hours__day">Sat</td><td>8 am - 10 pm</td></tr>
        <tr><td class="hours__day">Sun</td><td>Off</td></tr>
      </table>
    </div>
    <svg class="pin-icon" viewBox="0 0 20 20" aria-hidden="true">
      <rect width="20" height="20" rx="4" fill="var(--brand-blue)"/>
      <path d="M10,3.5 a4.5,4.5 0 0 1 4.5,4.5 c0,3.2 -4.5,8 -4.5,8 s-4.5,-4.8 -4.5,-8 a4.5,4.5 0 0 1 4.5,-4.5 z" fill="#fff"/>
      <circle cx="10" cy="8" r="1.7" fill="var(--brand-blue)"/>
    </svg>
    <address class="address" style="font-style:normal">
      Upper Level<span class="address__sep"></span>Harbour Court<br>
      Wrenfield Plaza Shopping Centre<br>
      Wrenfield Hill<span class="address__sep"></span>NSW 2190<br>
      P: 02 5550 1400&nbsp; F: 02 5550 1433
    </address>
  </section>

</main>
</body>
</html>
```